BRCW Business Cards

Business Cards should contain:
Bright Ridgecrest Coating Works
Felix Darrow
M: 0417 865 093
E: brightRCW@fernpost.example
BRCW logo
TCG logo
Painting & Decorating
Licence # 719362K
slogan: see the shine of every careful coat

Target Market(s)

all aspect of painting

Industry/Entity Type

Trade

Contact Information for Business Card

Felix Darrow
M: 0417 865 093
E: brightRCW@fernpost.example
BRCW logo
TCG logo
Painting & Decorating
Licence # 719362K

Font styles to use
Serif
Sans Serif

Requirements
Must have
• clear design with nice backround
• two sides
• smal TCG logo
Nice to have
• easy to read
Should not have
• mess
• black
• plastics form

```html
<!DOCTYPE html>
<html lang="en">
<head>
<meta charset="utf-8">
<title>BRCW Business Cards</title>
<link rel="stylesheet" href="https://fonts.googleapis.com/css2?family=Lora:ital,wght@0,500;1,400&family=Mulish:wght@400&display=swap">
<style>
  :root {
    --page-bg: #ece8e3;
    --card-bg: #ffffff;
    --ink: #1f1f1f;
    --ink-soft: #555555;
    --brand-teal: #1d4f4a;
    --brand-green: #3d8a2a;
    --accent-orange: #e8501e;
    --badge-blue: #2b4fa0;
    --mark-faint-a: #eef0ec;
    --mark-faint-b: #f7f7f5;
  }
  html, body {
    margin: 0;
    padding: 0;
    width: 1200px;
    height: 658px;
    overflow: hidden;
    background: var(--page-bg);
  }
  .canvas {
    position: relative;
    width: 1200px;
    height: 658px;
  }
  .card {
    position: absolute;
    background: var(--card-bg);
    border-radius: 9px;
    box-shadow: 0 4px 14px rgba(0,0,0,0.18);
    overflow: hidden;
  }
  .card--front { left: 95px; top: 88px; width: 444px; height: 259px; }
  .card--back  { left: 609px; top: 306px; width: 447px; height: 260px; }

  .faint-mark {
    position: absolute;
    border-radius: 40px 40px 12px 12px;
    background: linear-gradient(180deg, var(--mark-faint-a), var(--mark-faint-b));
  }
  .card--front .faint-mark { left: 18px; top: 19px; width: 162px; height: 226px; }
  .card--back .faint-mark  { left: 308px; top: 20px; width: 120px; height: 120px; }

  .slogan {
    position: absolute;
    left: 0; right: 0; top: 104px;
    text-align: center;
    font-family: "Lora", Georgia, serif;
    font-style: italic;
    font-size: 21px;
    color: var(--ink);
    margin: 0;
  }
  .service {
    position: absolute;
    left: 0; right: 0; top: 138px;
    text-align: center;
    font-family: "Mulish", Arial, sans-serif;
    font-size: 13px;
    color: var(--ink-soft);
    margin: 0;
  }
  .partner-badge {
    position: absolute;
    left: 266px; top: 190px;
    width: 50px; height: 36px;
  }
  .wordmark {
    position: absolute;
    display: flex;
    align-items: center;
    font-family: "Lora", Georgia, serif;
    font-weight: 500;
    color: var(--brand-teal);
    white-space: nowrap;
  }
  .wordmark__square { background: var(--brand-green); flex: none; }
  .card--front .wordmark { left: 336px; top: 196px; font-size: 17px; gap: 6px; }
  .card--front .wordmark__square { width: 14px; height: 14px; }
  .card--back .wordmark { left: 33px; top: 32px; font-size: 36px; gap: 12px; }
  .card--back .wordmark__square { width: 44px; height: 44px; }

  .company-name {
    position: absolute;
    left: 90px; top: 80px;
    margin: 0;
    font-family: "Lora", Georgia, serif;
    font-weight: 500;
    font-size: 14px;
    line-height: 17px;
    color: var(--brand-teal);
    width: 140px;
  }

  .person-name {
    position: absolute;
    right: 31px; top: 137px;
    margin: 0;
    font-family: "Mulish", Arial, sans-serif;
    font-size: 21px;
    letter-spacing: 0.5px;
    color: var(--accent-orange);
  }
  .contact-list {
    position: absolute;
    right: 29px; top: 170px;
    margin: 0; padding: 0;
    list-style: none;
    font-family: "Mulish", Arial, sans-serif;
    font-size: 13.5px;
    color: var(--ink);
  }
  .contact-list li {
    display: flex;
    justify-content: flex-end;
    align-items: center;
    gap: 10px;
    height: 22px;
  }
  .contact-icon { width: 12px; height: 13px; flex: none; }
</style>
</head>
<body>
<main class="canvas">

  <section class="card card--front" aria-label="Card front">
    <div class="faint-mark" role="img" aria-label="Faint brand mark decoration"></div>
    <p class="slogan">see the shine of every careful coat</p>
    <p class="service">Painting &amp; Decorating</p>
    <svg class="partner-badge" viewBox="0 0 50 36" role="img" aria-label="TCG association badge">
      <rect x="0" y="0" width="50" height="36" rx="3" fill="var(--badge-blue)" opacity="0.85"/>
    </svg>
    <div class="wordmark"><span class="wordmark__square"></span>BRCW</div>
  </section>

  <section class="card card--back" aria-label="Card back">
    <div class="faint-mark" role="img" aria-label="Faint brand mark decoration"></div>
    <div class="wordmark"><span class="wordmark__square"></span>BRCW</div>
    <p class="company-name">Bright Ridgecrest Coating Works</p>

    <p class="person-name">FELIX DARROW</p>
    <ul class="contact-list">
      <li>0417 865 093
        <svg class="contact-icon" viewBox="0 0 12 13" aria-hidden="true">
          <rect x="2.5" y="0.5" width="7" height="12" rx="1.5" fill="none" stroke="var(--accent-orange)" stroke-width="1.2"/>
          <line x1="5" y1="10.3" x2="7" y2="10.3" stroke="var(--accent-orange)" stroke-width="1.2"/>
        </svg>
      </li>
      <li>brightRCW@fernpost.example
        <svg class="contact-icon" viewBox="0 0 12 13" aria-hidden="true">
          <rect x="0.6" y="3" width="10.8" height="7.5" fill="none" stroke="var(--accent-orange)" stroke-width="1.2"/>
          <polyline points="0.6,3 6,7.5 11.4,3" fill="none" stroke="var(--accent-orange)" stroke-width="1.2"/>
        </svg>
      </li>
      <li>Licence # 719362K
        <svg class="contact-icon" viewBox="0 0 12 13" aria-hidden="true">
          <circle cx="6" cy="4.5" r="3.6" fill="none" stroke="var(--accent-orange)" stroke-width="1.2"/>
          <polyline points="3.8,7.5 3.8,12.3 6,10.8 8.2,12.3 8.2,7.5" fill="none" stroke="var(--accent-orange)" stroke-width="1.2"/>
        </svg>
      </li>
    </ul>
  </section>

</main>
</body>
</html>
```